Biz Card for Harrowfield Property Partners - HWPP

Harrowfield Property Partners is a commercial real estate acquisitions firm. We buy commercial property and need to raise capital from investors for each deal we buy. The vibe needs to be: give us your money, we will multiply it.
Our website: www.hrwpp-example.com
Competitors are: https://velmarholdings-example.com/, https://tribanquepartners-example.com/, http://www.ostrellecapital-example.com/
Target Market(s)
High Net Worth Individuals, Bankers, Insurance Companies, Commercial Real Estate Brokers.
Industry/Entity Type
Investment Banking
Contact Information for Business Card
Name, Title, Addess, Cell#, Office#, email, website
Requirements
Must have
- use one of our logos. See website for look and feel: www.hrwpp-example.com
Nice to have
- see website: www.hrwpp-example.com

```html
<!DOCTYPE html>
<html lang="en">
<head>
<meta charset="utf-8">
<title>Harrowfield Property Partners – Business Card</title>
<link href="https://fonts.googleapis.com/css2?family=Source+Sans+3:wght@400;600;700&display=swap" rel="stylesheet">
<style>
  :root {
    --navy: #0b2a4a;
    --paper: #ffffff;
    --ink-grey: #6d7f93;
    --stage-top: #0f4a7a;
    --stage-bottom: #061a30;
    --card-w: 540px;
    --card-h: 310px;
    --cell-w: 270px;
    --cell-h: 103.33px;
  }
  * { box-sizing: border-box; margin: 0; padding: 0; }
  html, body {
    width: 1200px; height: 900px; overflow: hidden;
  }
  body {
    background: radial-gradient(ellipse at 50% 40%, var(--stage-top), var(--stage-bottom));
    font-family: "Source Sans 3", "Myriad Pro", sans-serif;
    display: flex; align-items: center; justify-content: center; gap: 40px;
  }
  .card {
    position: relative;
    width: var(--card-w); height: var(--card-h);
    background: var(--paper);
    overflow: hidden;
    box-shadow: 0 18px 40px rgba(0,0,0,.45);
  }

  /* Front */
  .front .block { position: absolute; background: var(--navy); }
  .front .block-corner { left: 0; top: 0; width: 100px; height: 100px; }
  .front .block-middle { left: 100px; top: 100px; width: 100px; height: 100px; }
  .front .block-edge { left: 0; top: 200px; width: 40px; height: 110px; }
  .front .block-foot { right: 0; bottom: 0; width: 90px; height: 70px; }
  .brand {
    position: absolute; left: 220px; top: 150px;
    display: flex; align-items: center; gap: 14px;
  }
  .brand-dot { width: 54px; height: 54px; border-radius: 50%; background: var(--navy); flex: none; }
  .brand-name {
    color: var(--navy); font-weight: 600; font-size: 21px;
    letter-spacing: .16em; text-transform: uppercase; line-height: 1.15;
  }

  /* Back */
  .back { display: grid; grid-template-columns: 1fr 1fr; grid-template-rows: repeat(3, 1fr); }
  .cell { display: flex; flex-direction: column; justify-content: center; padding: 0 28px; font-size: 14px; }
  .cell.dark { background: var(--navy); color: var(--paper); }
  .cell.light { background: var(--paper); color: var(--navy); }
  .contact-line { display: flex; align-items: center; gap: 10px; }
  .contact-line svg { flex: none; }
  .person-name { font-size: 22px; font-weight: 700; line-height: 1.1; }
  .person-title { font-size: 12px; letter-spacing: .06em; text-transform: uppercase; }
  .address { line-height: 1.35; }
</style>
</head>
<body>

  <section class="card front" aria-label="Card front">
    <div class="block block-corner"></div>
    <div class="block block-middle"></div>
    <div class="block block-edge"></div>
    <div class="block block-foot"></div>
    <div class="brand">
      <span class="brand-dot"></span>
      <span class="brand-name">Harrowfield<br>Property Partners</span>
    </div>
  </section>

  <section class="card back" aria-label="Card back">
    <div class="cell dark">
      <div class="contact-line">
        <svg width="16" height="12" viewBox="0 0 16 12" aria-hidden="true">
          <rect x="0.75" y="0.75" width="14.5" height="10.5" fill="none" stroke="currentColor" stroke-width="1.2"/>
          <polyline points="1,1 8,7 15,1" fill="none" stroke="currentColor" stroke-width="1.2"/>
        </svg>
        <span>dmarsh@hrwpp-example.com</span>
      </div>
    </div>
    <div class="cell light"></div>

    <div class="cell light">
      <div class="person-name">Daniel Marsh</div>
      <div class="person-title">Managing Partner</div>
    </div>
    <div class="cell dark">
      <div class="contact-line"><span>(555) 014-2290</span></div>
    </div>

    <div class="cell dark">
      <div class="address">418 Linden Row, Suite 900<br>Marlow Park, FL 00000</div>
    </div>
    <div class="cell light"></div>
  </section>

</body>
</html>
```